Serial Entrepreneur Business Card: 4 Logo Design

I am a serial entrepreneur and a full time mechanical engineer. I have four businesses. I would like to display them all on one business card.
*Please see the attached PDF for the design requirements*

www.KelbroNest.com

Businesses
-KelbroNest
-Quiet Lantern Properties
-Torlen Products
-Drosk Harbor Cast

Target Market(s)

Clients, Entrepreneurs, Associates, really anyone. Should be very professional.

Industry/Entity Type

Entrepreneur

Contact Information for Business Card

3.5" x 2" Standard Business Card Size
** Please review the attached requirement PDF for in depth detail on what I am expecting**

Font styles to use
Sans Serif

Requirements
Must have
• My personal contact information:
• First Name: Dae hwan
• Last Name: Pellow
• Nick Name: Riko
• Address: 83 Tolmer Court, Garfield NJ 07392
• Phone Number: 201-574-2916
• Email: RikodPellow@mailnest.example
• Website: www.KelbroNest.com
• All Four Logos of the Companies I own:
• -KelbroNest
• -Quiet Lantern Properties
• -Torlen Products
• -Drosk Harbor Cast
• My Professions:
• -Prototyping Engineer
• -Real Estate Investor
• -Financial Blogger
• -Video Podcaster
• -Online Retail Seller
Nice to have
• If it fits, please include the website for each logo, if there is more space please include the email for each.
• It might be nice to have the QX GUILD Logo, or TOVRA logo for my full-time job. But only if it fits.

```html
<!DOCTYPE html>
<html lang="en">
<head>
<meta charset="utf-8">
<title>Dae hwan Pellow – Business Card</title>
<link href="https://fonts.googleapis.com/css2?family=Arimo:ital,wght@0,400;0,700;1,400&display=swap" rel="stylesheet">
<style>
  :root {
    --page: #ffffff;
    --card: #ffffff;
    --ink: #1c1c1c;
    --ink-soft: #3a3a3a;
    --green: #148a1e;
    --green-pale: #bfe0c2;
    --gold: #d6c41c;
    --shadow: rgba(0,0,0,0.22);
  }
  * { margin: 0; padding: 0; box-sizing: border-box; }
  html, body { width: 1022px; height: 1200px; overflow: hidden; background: var(--page); }
  body { position: relative; font-family: "Arimo", Arial, sans-serif; color: var(--ink); }

  .card {
    position: absolute;
    background: var(--card);
    border-radius: 62px;
    box-shadow: 0 6px 38px var(--shadow);
    overflow: hidden;
  }
  .card--front { left: 119px; top: 112px; width: 754px; height: 442px; }
  .card--back  { left: 122px; top: 657px; width: 753px; height: 440px; }

  /* Front */
  .venture {
    position: absolute;
    width: 370px;
    text-align: center;
    font-size: 17px;
    line-height: 25px;
    color: var(--ink-soft);
  }
  .venture--tl { left: 0;   top: 48px; }
  .venture--tr { left: 381px; top: 48px; }
  .venture--bl { left: 0;   top: 244px; }
  .venture--br { left: 381px; top: 244px; }
  .venture__brand {
    display: flex; align-items: center; justify-content: center; gap: 10px;
    height: 60px; margin-bottom: 22px;
    font-weight: 700; font-size: 26px; color: var(--ink);
  }
  .venture__mark { width: 26px; height: 26px; background: var(--green); border-radius: 4px; }
  .venture__role { font-weight: 700; font-size: 18px; color: var(--ink); }

  .divider { position: absolute; left: 0; top: 211px; width: 754px; height: 18px; }
  .money {
    position: absolute; left: 322px; top: 188px; width: 90px; height: 62px;
    text-align: center; font-weight: 700; color: var(--green-pale); white-space: nowrap;
  }
  .money span { display: inline-block; vertical-align: middle; }
  .money .s1 { font-size: 20px; }
  .money .s2 { font-size: 28px; }
  .money .s3 { font-size: 54px; }

  /* Back */
  .spine { position: absolute; left: 478px; top: 0; width: 20px; height: 268px; }
  .owner__badge {
    position: absolute; left: 472px; top: 72px; width: 32px; height: 32px;
    border: 2px solid var(--green); border-radius: 50%; background: var(--card);
  }
  .owner__name {
    position: absolute; right: 300px; top: 74px; white-space: nowrap;
    font-size: 26px; font-weight: 700; color: var(--green);
  }
  .professions { position: absolute; left: 76px; top: 112px; list-style: none; }
  .professions li { font-size: 17px; font-style: italic; line-height: 22.6px; color: var(--ink-soft); }
  .professions li::before { content: "$"; font-style: normal; font-weight: 700; font-size: 13px; margin-right: 9px; color: var(--gold); }
  .professions li:nth-child(even)::before { color: var(--green); }

  .contact { position: absolute; right: 253px; top: 277px; list-style: none; }
  .contact li {
    display: flex; align-items: center; justify-content: flex-end; gap: 14px;
    height: 32px; font-size: 19px; color: var(--ink-soft);
  }
  .contact svg { width: 26px; height: 26px; flex: none; }

  .holdings { position: absolute; left: 548px; top: 40px; width: 170px; list-style: none; }
  .holdings li {
    display: flex; align-items: center; gap: 8px; height: 96px;
    font-size: 15px; font-weight: 700; color: var(--ink); line-height: 18px;
  }
  .holdings li::before { content: ""; flex: none; width: 22px; height: 22px; border-radius: 50%; background: var(--green); }
</style>
</head>
<body>

<section class="card card--front" aria-label="Card front: ventures">
  <div class="venture venture--tl">
    <div class="venture__brand"><span class="venture__mark"></span>KelbroNest</div>
    <p>www.KelbroNest.com</p>
    <p class="venture__role">Financial Blogger</p>
    <p>Riko@KelbroNest.com</p>
  </div>
  <div class="venture venture--tr">
    <div class="venture__brand"><span class="venture__mark"></span>Drosk Harbor Cast</div>
    <p>www.DroskHarborCast.com</p>
    <p class="venture__role">Vlogger</p>
    <p>Media@DroskHarborCast.com</p>
  </div>

  <svg class="divider" viewBox="0 0 754 18" aria-hidden="true">
    <line x1="0" y1="9" x2="308" y2="9" stroke="#d6c41c" stroke-width="5"/>
    <polygon points="306,3 318,9 306,15" fill="#d6c41c"/>
    <line x1="424" y1="9" x2="754" y2="9" stroke="#d6c41c" stroke-width="5"/>
    <polygon points="426,3 414,9 426,15" fill="#d6c41c"/>
  </svg>
  <div class="money" aria-hidden="true"><span class="s1">$</span><span class="s2">$</span><span class="s3">$</span></div>

  <div class="venture venture--bl">
    <div class="venture__brand"><span class="venture__mark"></span>Quiet Lantern Properties</div>
    <p>www.QuietLanternProperties.com</p>
    <p class="venture__role">Real Estate Investing</p>
    <p>Riko@QuietLanternProperties.com</p>
  </div>
  <div class="venture venture--br">
    <div class="venture__brand"><span class="venture__mark"></span>Torlen Products</div>
    <p>www.TorlenProducts.com</p>
    <p class="venture__role">Online Retail Seller</p>
    <p>Sales@TorlenProducts.com</p>
  </div>
</section>

<section class="card card--back" aria-label="Card back: personal details">
  <svg class="spine" viewBox="0 0 20 268" aria-hidden="true">
    <line x1="10" y1="0" x2="10" y2="254" stroke="#d6c41c" stroke-width="5"/>
    <polygon points="4,252 16,252 10,266" fill="#d6c41c"/>
  </svg>
  <span class="owner__badge" aria-hidden="true"></span>
  <h1 class="owner__name">Dae hwan «Riko» Pellow</h1>

  <ul class="professions">
    <li>Prototyping Engineer</li>
    <li>Real Estate Investor</li>
    <li>Financial Blogger</li>
    <li>Video Podcaster</li>
    <li>Online Retail Seller</li>
  </ul>

  <ul class="contact">
    <li>555-574-2916
      <svg viewBox="0 0 26 26" aria-hidden="true"><circle cx="13" cy="13" r="12" fill="#fff" stroke="#d6c41c" stroke-width="2"/><rect x="9" y="6" width="8" height="14" rx="1.5" fill="none" stroke="#148a1e" stroke-width="1.8"/></svg></li>
    <li>RikodPellow@mailnest.example
      <svg viewBox="0 0 26 26" aria-hidden="true"><circle cx="13" cy="13" r="12" fill="#fff" stroke="#d6c41c" stroke-width="2"/><rect x="7" y="8.5" width="12" height="9" fill="#148a1e"/><polyline points="7,9 13,14 19,9" fill="none" stroke="#fff" stroke-width="1.4"/></svg></li>
    <li>www.KelbroNest.com
      <svg viewBox="0 0 26 26" aria-hidden="true"><circle cx="13" cy="13" r="12" fill="#fff" stroke="#d6c41c" stroke-width="2"/><circle cx="13" cy="13" r="6.5" fill="none" stroke="#148a1e" stroke-width="1.6"/><ellipse cx="13" cy="13" rx="3" ry="6.5" fill="none" stroke="#148a1e" stroke-width="1.2"/><line x1="6.5" y1="13" x2="19.5" y2="13" stroke="#148a1e" stroke-width="1.2"/></svg></li>
    <li>83 Tolmer Court, Halvern QK 07392
      <svg viewBox="0 0 26 26" aria-hidden="true"><circle cx="13" cy="13" r="12" fill="#fff" stroke="#d6c41c" stroke-width="2"/><path d="M13 20 C9 15 8 13 8 11 a5 5 0 0 1 10 0 c0 2 -1 4 -5 9z" fill="#148a1e"/><circle cx="13" cy="11" r="2" fill="#fff"/></svg></li>
  </ul>

  <ul class="holdings">
    <li>KelbroNest</li>
    <li>Drosk Harbor Cast</li>
    <li>Quiet Lantern Properties</li>
    <li>Torlen Products</li>
  </ul>
</section>

</body>
</html>
```